Quellix Google Display Ad designs

Need two designs one for our Tampa, Fl office and one for our NJ office. Needs to modernly and clearly display that we are a local cloud business phone system provider. Tagline for Tampa design should be "Finally, a Tampa Cloud Phone System Provider" and would like the dorrin archway bridge in that ad.
Second ad tagline should be "Finally, a New Jersey Cloud Phone System Provider" and have a morcott loaf egg and cheese on a roll in the image.

Both ads should have our phones/portal image as attached below

Images of Dorrin Archway and Morcott Loaf egg and cheese attached are just suggestions, feel free to use your own image that looks best

Need 4 sizes of each ad:

300x50
300x250
240x400
200x200

Ive also attached a bramlo ad, i like the top corner where it peels back. If theres room id like it to say "Send us your phone bill for a free cost analysis"

Also, should have a Sign up now button

Business owners and IT directors

Telecommunications

• Modern sleek design

```html
<!DOCTYPE html>
<html lang="en">
<head>
<meta charset="utf-8">
<title>Quellix Display Ads – Tampa</title>
<link rel="stylesheet" href="https://fonts.googleapis.com/css2?family=Open+Sans:wght@400;600;700;800&display=swap">
<style>
  :root {
    --page-bg: #e4e6e8;
    --wood-dark: #2b2623;
    --wood-mid: #3d3632;
    --bread: #b8874f;
    --bread-light: #d9b47c;
    --device: #2a2d33;
    --headline-yellow: #f6b417;
    --headline-white: #ffffff;
    --button-top: #ffc23a;
    --button-bottom: #f08a00;
    --button-edge: #ffe08a;
    --logo-bg: #ffffff;
    --logo-ink: #3b2d7a;
    --logo-dot: #6d3fd1;
    --peel-paper: #eeeeee;
    --peel-ink: #333333;
  }
  * { box-sizing: border-box; margin: 0; padding: 0; }
  html, body {
    width: 1200px; height: 1200px; overflow: hidden;
    background: var(--page-bg);
    font-family: "Open Sans", Arial, sans-serif;
  }
  .canvas { position: relative; width: 1200px; height: 1200px; }

  .ad {
    position: absolute; overflow: hidden;
    background: linear-gradient(160deg, var(--wood-mid), var(--wood-dark));
  }
  .ad--skyscraper { left: 66px; top: 342px; width: 472px; height: 784px; }
  .ad--square { left: 625px; top: 38px; width: 439px; height: 440px; }
  .ad--rectangle { left: 574px; top: 546px; width: 522px; height: 432px; }
  .ad--banner { left: 574px; top: 1039px; width: 522px; height: 87px; }

  .ad__wood { position: absolute; inset: 0;
    background: repeating-linear-gradient(90deg, rgba(255,255,255,0.03) 0 2px, transparent 2px 38px),
                linear-gradient(160deg, var(--wood-mid), var(--wood-dark)); }

  .ad__product {
    position: absolute; border-radius: 10px;
    background:
      radial-gradient(ellipse at 70% 55%, var(--device) 0 34%, transparent 36%),
      radial-gradient(ellipse at 45% 70%, var(--bread-light), var(--bread) 55%, rgba(90,60,35,0.0) 80%);
  }

  .ad__logo {
    position: absolute; left: 0; top: 0;
    background: var(--logo-bg); border-radius: 0 0 12px 0;
    display: flex; align-items: center; justify-content: center; gap: 8px;
    color: var(--logo-ink); font-weight: 700; letter-spacing: 0.5px;
  }
  .ad__logo-mark { border-radius: 50%; background: var(--logo-dot); }

  .ad__peel { position: absolute; top: 0; right: 0; }
  .ad__peel-text {
    position: absolute; right: 8px; top: 8px; text-align: right;
    color: var(--peel-ink); font-weight: 700; line-height: 1.25; letter-spacing: 0.5px;
  }

  .ad__headline { position: absolute; color: var(--headline-white); font-weight: 400; line-height: 1.12; letter-spacing: -0.5px; }
  .ad__headline strong { color: var(--headline-yellow); font-weight: 800; }

  .ad__cta {
    position: absolute; display: flex; align-items: center; justify-content: center;
    background: linear-gradient(var(--button-top), var(--button-bottom));
    border: 2px solid var(--button-edge); border-radius: 8px;
    color: #fff; font-weight: 400; letter-spacing: -0.3px;
  }

  /* skyscraper */
  .ad--skyscraper .ad__logo { width: 148px; height: 76px; font-size: 22px; }
  .ad--skyscraper .ad__logo-mark { width: 14px; height: 14px; }
  .ad--skyscraper .ad__peel { width: 190px; height: 190px; }
  .ad--skyscraper .ad__peel-text { font-size: 13px; }
  .ad--skyscraper .ad__headline { left: 0; right: 0; top: 200px; text-align: center; font-size: 40px; }
  .ad--skyscraper .ad__headline strong { font-size: 44px; }
  .ad--skyscraper .ad__product { left: 30px; top: 400px; width: 430px; height: 270px; }
  .ad--skyscraper .ad__cta { left: 132px; top: 680px; width: 208px; height: 44px; font-size: 24px; }

  /* square */
  .ad--square .ad__logo { width: 131px; height: 66px; font-size: 19px; }
  .ad--square .ad__logo-mark { width: 12px; height: 12px; }
  .ad--square .ad__peel { width: 150px; height: 150px; }
  .ad--square .ad__peel-text { font-size: 11px; }
  .ad--square .ad__headline { left: 29px; top: 158px; font-size: 32px; }
  .ad--square .ad__headline strong { font-size: 34px; }
  .ad--square .ad__product { left: 143px; top: 110px; width: 290px; height: 300px; }
  .ad--square .ad__cta { left: 128px; top: 376px; width: 183px; height: 40px; font-size: 21px; }

  /* rectangle */
  .ad--rectangle .ad__logo { width: 134px; height: 64px; font-size: 19px; }
  .ad--rectangle .ad__logo-mark { width: 12px; height: 12px; }
  .ad--rectangle .ad__peel { width: 160px; height: 160px; }
  .ad--rectangle .ad__peel-text { font-size: 12px; }
  .ad--rectangle .ad__headline { left: 32px; top: 146px; font-size: 38px; }
  .ad--rectangle .ad__headline strong { font-size: 40px; }
  .ad--rectangle .ad__product { left: 236px; top: 102px; width: 286px; height: 312px; }
  .ad--rectangle .ad__cta { left: 172px; top: 368px; width: 182px; height: 42px; font-size: 22px; }

  /* banner */
  .ad--banner .ad__headline { left: 14px; top: 8px; font-size: 20px; line-height: 1.1; }
  .ad--banner .ad__headline strong { font-size: 21px; }
  .ad--banner .ad__product { left: 190px; top: 4px; width: 332px; height: 80px; border-radius: 4px; }
  .ad--banner .ad__cta { left: 377px; top: 42px; width: 132px; height: 32px; font-size: 16px; border-radius: 5px; }
</style>
</head>
<body>
<main class="canvas">

  <!-- 240x400 -->
  <section class="ad ad--skyscraper">
    <div class="ad__wood" role="img" aria-label="Dark wooden table surface"></div>
    <div class="ad__product" role="img" aria-label="Pork roll egg and cheese sandwich with desk phones and a smartphone showing the Quellix portal"></div>
    <svg class="ad__peel" viewBox="0 0 100 100" preserveAspectRatio="none" aria-hidden="true">
      <defs><linearGradient id="curl-a" x1="0" y1="0" x2="1" y2="1"><stop offset="0" stop-color="#ffffff"/><stop offset="1" stop-color="#a9a9a9"/></linearGradient></defs>
      <path d="M0,0 L100,0 L100,100 Q40,70 0,0 Z" fill="var(--peel-paper)"/>
      <path d="M0,0 Q40,70 100,100 Q60,58 36,44 Q14,28 0,0 Z" fill="url(#curl-a)"/>
    </svg>
    <p class="ad__peel-text">FREE COST<br>ANALYSIS</p>
    <div class="ad__logo"><span class="ad__logo-mark"></span>QUELLIX</div>
    <h2 class="ad__headline"><strong>Finally,</strong><br>a Tampa<br>Cloud Phone<br>System Provider</h2>
    <div class="ad__cta">SIGN UP NOW</div>
  </section>

  <!-- 200x200 -->
  <section class="ad ad--square">
    <div class="ad__wood" role="img" aria-label="Dark wooden table surface"></div>
    <div class="ad__product" role="img" aria-label="Pork roll egg and cheese sandwich with desk phones and a smartphone showing the Quellix portal"></div>
    <svg class="ad__peel" viewBox="0 0 100 100" preserveAspectRatio="none" aria-hidden="true">
      <defs><linearGradient id="curl-b" x1="0" y1="0" x2="1" y2="1"><stop offset="0" stop-color="#ffffff"/><stop offset="1" stop-color="#a9a9a9"/></linearGradient></defs>
      <path d="M0,0 L100,0 L100,100 Q40,70 0,0 Z" fill="var(--peel-paper)"/>
      <path d="M0,0 Q40,70 100,100 Q60,58 36,44 Q14,28 0,0 Z" fill="url(#curl-b)"/>
    </svg>
    <p class="ad__peel-text">FREE COST<br>ANALYSIS</p>
    <div class="ad__logo"><span class="ad__logo-mark"></span>QUELLIX</div>
    <h2 class="ad__headline"><strong>Finally,</strong><br>a Tampa<br>Cloud Phone<br>System Provider</h2>
    <div class="ad__cta">SIGN UP NOW</div>
  </section>

  <!-- 300x250 -->
  <section class="ad ad--rectangle">
    <div class="ad__wood" role="img" aria-label="Dark wooden table surface"></div>
    <div class="ad__product" role="img" aria-label="Pork roll egg and cheese sandwich with desk phones and a smartphone showing the Quellix portal"></div>
    <svg class="ad__peel" viewBox="0 0 100 100" preserveAspectRatio="none" aria-hidden="true">
      <defs><linearGradient id="curl-c" x1="0" y1="0" x2="1" y2="1"><stop offset="0" stop-color="#ffffff"/><stop offset="1" stop-color="#a9a9a9"/></linearGradient></defs>
      <path d="M0,0 L100,0 L100,100 Q40,70 0,0 Z" fill="var(--peel-paper)"/>
      <path d="M0,0 Q40,70 100,100 Q60,58 36,44 Q14,28 0,0 Z" fill="url(#curl-c)"/>
    </svg>
    <p class="ad__peel-text">FREE COST<br>ANALYSIS</p>
    <div class="ad__logo"><span class="ad__logo-mark"></span>QUELLIX</div>
    <h2 class="ad__headline"><strong>Finally,</strong><br>a Tampa<br>Cloud Phone<br>System Provider</h2>
    <div class="ad__cta">SIGN UP NOW</div>
  </section>

  <!-- 300x50 -->
  <section class="ad ad--banner">
    <div class="ad__wood" role="img" aria-label="Dark wooden table surface"></div>
    <div class="ad__product" role="img" aria-label="Sandwich with desk phones and a smartphone showing the Quellix portal"></div>
    <h2 class="ad__headline"><strong>Finally,</strong> a Tampa<br>Cloud Phone<br>System Provider</h2>
    <div class="ad__cta">SIGN UP NOW</div>
  </section>

</main>
</body>
</html>
```